Wordpress design for my private practice website - Psychotherapist

I would like a simple, clean, and elegant design for my private practice website. I work with both adults and children so I'd like it to appeal to both. However, since parents make the choice as to where to send their child for therapy, I want it to appeal to adults more. I would like the pictures on the site to have a calming effect - maybe using sand and water and rocks. I am attaching files with my company logo. I would also like my name incorporated into the header - Colette Brannigan, LCSW, Registered Play Therapist. I've also uploaded a picture of myself for my About Page.

I like the design of these 2 website and want something similar:
www.drlorapenwick.example
www.harwood-tallis.example

I would like a home page that highlights a calming graphic across the entire top of the page as well as my practice logo and my name.

I'd like a link to social media sites on the top of the homepage - facebook, pinterest.

I want a simple bar across the top with the following tabs:
Home
About Me (subtabs Who I Am, Specialties and Approach)
Counseling Services (subtabs Individual Counseling, Play Therapy, Sandplay Therapy,)
Fees
FAQs
Contact Me (would love this to be a fill in the blank contact form that sends info to my email address - should include name, phone number, email and a comment box for more information requested)
Blog (this will link with another wordpress blog)

Target Market(s)

Parents of children under age 12 with behavioral problems or are dealing with the breakup of their family through divorce - looking for someone to work with their young child. I also work with Adults that are overwhelmed and worried - often women that have many life stressors and are feeling burnt out on life and meeting everyone's needs. Families going through some type of trauma, including divorce or grief work. I also work with individuals going through a transition of religious beliefs - often exiting the religion of their youth and undergoing a crisis of faith at midlife.

Industry/Entity Type

Mental Health

Contact Information for Business Card

Colette Brannigan, LCSW
Registered Play Therapist
4917 Wexmoor Lane
Idaho Falls, Idaho 83404
(208)555-0187
www.stillbrookcounseling.example

On the opposite side, I'd like an appointment reminder area - with the following text:

Your next appointment is
_____/______/______ at ______am/pm
Please give 24 hrs notice if you need to cancel your appointment.

Coding

Coded - Design and coding required

Number of Pages Required

5+ page

Font styles to use
Sans Serif

Colors
33a6d7
9bcb3c
0355a3

Requirements
Must have
• I'd like it to be a wordpress site. I'm such a newby at web design - but I need to be able to add content and manage the site myself once it is up and running.
Nice to have
• I like the design of these 2 websites and want something similar:
• www.drlorapenwick.example
• www.harwood-tallis.example
• They are clean, easy to navigate and calming.
Should not have
• Should not look like a childcare website.

```html
<!DOCTYPE html>
<html lang="en">
<head>
<meta charset="utf-8">
<title>Colette Brannigan, LCSW – Stillbrook Counseling</title>
<link href="https://fonts.googleapis.com/css2?family=Open+Sans:wght@300;400;600&display=swap" rel="stylesheet">
<style>
  :root {
    --sky: #33a6d7;
    --leaf: #9bcb3c;
    --deep: #0355a3;
    --ink: #555a5e;
    --ink-soft: #8a8f93;
    --rule: #dedede;
    --white: #ffffff;
    --sand-light: #c9a487;
    --sand-dark: #a98064;
  }
  * { margin: 0; padding: 0; box-sizing: border-box; }
  html, body { width: 895px; height: 1200px; overflow: hidden; background: var(--white); }
  body { font-family: "Open Sans", Arial, sans-serif; color: var(--ink); position: relative; }

  .hero {
    position: absolute; left: 0; top: 0; width: 895px; height: 259px;
    background: radial-gradient(ellipse at 50% 60%, #cfab8e 0%, var(--sand-light) 45%, var(--sand-dark) 100%);
  }
  .hero-name {
    position: absolute; top: 100px; width: 100%; text-align: center;
    color: var(--white); font-weight: 600; font-size: 22px; letter-spacing: 0.5px;
  }
  .hero-title {
    position: absolute; top: 125px; width: 100%; text-align: center;
    color: rgba(255,255,255,0.75); font-size: 9.5px; letter-spacing: 4px;
  }

  .brand { position: absolute; top: 288px; width: 100%; text-align: center; }
  .brand-name { font-weight: 300; font-size: 26px; letter-spacing: 8px; color: #6a6e72; }
  .brand-sub { margin-top: 4px; font-size: 12px; letter-spacing: 5px; color: #6a6e72; }

  .main-nav {
    position: absolute; left: 94px; top: 377px; width: 708px; height: 33px;
    border-bottom: 1px solid var(--rule); display: flex;
  }
  .main-nav a {
    flex: auto; text-align: center; font-size: 10px; text-decoration: none; color: var(--ink);
    line-height: 25px; border-right: 1px solid var(--rule); height: 25px;
  }
  .main-nav a:last-child { border-right: none; }
  .main-nav a.current { color: var(--leaf); }

  .portrait {
    position: absolute; left: 110px; top: 446px; width: 188px; height: 225px;
    border: 3px solid var(--white); box-shadow: 0 0 3px rgba(0,0,0,0.25);
    background: linear-gradient(160deg, #d9c28a 0%, #b99a5c 50%, #6f8a48 100%);
  }
  .intro { position: absolute; left: 354px; top: 447px; width: 430px; text-align: justify; }
  .intro-lead { font-size: 11.2px; line-height: 20px; color: var(--ink); }
  .intro-body { margin-top: 20px; font-size: 10px; line-height: 20px; color: var(--ink-soft); }

  .divider {
    position: absolute; left: 94px; top: 708px; width: 708px; height: 1px; background: var(--rule);
    box-shadow: 0 2px 3px rgba(0,0,0,0.06);
  }

  .feature { position: absolute; top: 742px; width: 200px; text-align: center; }
  .feature-icon { display: block; margin: 0 auto; }
  .feature-title { margin-top: 14px; font-size: 12px; font-weight: 600; letter-spacing: 0.5px; color: #66696c; }
  .feature-text { margin-top: 18px; font-size: 9.3px; line-height: 17px; color: var(--ink-soft); padding: 0 10px; }
  .feature-btn {
    display: inline-block; margin-top: 16px; width: 64px; height: 24px; line-height: 21px;
    border: 1.5px solid var(--leaf); border-radius: 12px; font-size: 8.5px; color: var(--leaf);
    text-decoration: none; box-shadow: 0 2px 2px rgba(0,0,0,0.12);
  }

  .footer-wave { position: absolute; left: 0; top: 990px; }
  .footer { position: absolute; left: 0; top: 1090px; width: 100%; text-align: center; color: var(--white); }
  .social { display: flex; justify-content: center; gap: 16px; }
  .social span { width: 12px; height: 12px; border-radius: 50%; background: var(--white); display: block; }
  .footer-links { margin-top: 19px; font-size: 8.5px; word-spacing: 2px; }
  .footer-links span { margin: 0 12px; }
  .copyright { margin-top: 20px; font-size: 8.5px; }
</style>
</head>
<body>
  <header class="hero" role="img" aria-label="Calm photograph of smooth dark pebbles resting on rippled sand">
    <h1 class="hero-name">COLETTE BRANNIGAN, LCSW</h1>
    <p class="hero-title">Registered Play Therapist</p>
  </header>

  <div class="brand">
    <div class="brand-name">STILLBROOK</div>
    <div class="brand-sub">COUNSELING</div>
  </div>

  <nav class="main-nav">
    <a class="current" href="#">HOME</a>
    <a href="#">ABOUT ME</a>
    <a href="#">COUNSELING SERVICES</a>
    <a href="#">FEES</a>
    <a href="#">FAQS</a>
    <a href="#">CONTACT</a>
    <a href="#">BLOG</a>
  </nav>

  <div class="portrait" role="img" aria-label="Portrait photograph of the therapist outdoors in golden grass"></div>

  <section class="intro">
    <p class="intro-lead">If you're looking for extra support and guidance through a challenging situation or you're just ready to move in a new direction in your life, I look forward to working with you to achieve your goals.</p>
    <p class="intro-body">Lorem ipsum dolor sit amet, consectetur adipiscing elit. Mauris sed elementum arcu. Donec cursus ornare ipsum. Vestibulum dapibus vitae ante id finibus. Nulla ultrices suscipit leo, ut molestie sapien ornare vitae. Nisl vel arcu pellentesque elementum. Duis convallis nulla elit, in mollis nisl tristique et. Pellentesque at imperdiet ante. Lorem ipsum dolor sit amet, consectetur adipiscing elit. Mauris sed elementum arcu. Donec cursus ornare ipsum. Vestibulum dapibus vitae ante id finibus. Nulla ultrices suscipit leo, ut molestie sapien ornare vitae. Nisl vel arcu pellentesque elementum. Duis convallis nulla elit, in mollis nisl tristique et.</p>
  </section>

  <div class="divider"></div>

  <section class="feature" style="left:102px">
    <svg class="feature-icon" width="98" height="98" viewBox="0 0 98 98" fill="none" stroke="var(--leaf)" stroke-width="1.6">
      <circle cx="49" cy="49" r="47.5"/>
      <rect x="31" y="34" width="36" height="32" rx="2"/>
      <line x1="31" y1="42" x2="67" y2="42"/>
      <line x1="38" y1="30" x2="38" y2="37"/><line x1="60" y1="30" x2="60" y2="37"/>
      <g fill="var(--leaf)" stroke="none">
        <rect x="37" y="46" width="5" height="4"/><rect x="46.5" y="46" width="5" height="4"/><rect x="56" y="46" width="5" height="4"/>
        <rect x="37" y="53" width="5" height="4"/><rect x="46.5" y="53" width="5" height="4"/><rect x="56" y="53" width="5" height="4"/>
      </g>
    </svg>
    <h2 class="feature-title">SCHEDULE APPOINTMENT</h2>
    <p class="feature-text">Start your new path in life and be the change today!</p>
    <a class="feature-btn" href="#">Click Here</a>
  </section>

  <section class="feature" style="left:349px">
    <svg class="feature-icon" width="98" height="98" viewBox="0 0 98 98" fill="none" stroke="var(--leaf)" stroke-width="1.6">
      <circle cx="49" cy="49" r="47.5"/>
      <circle cx="38" cy="45" r="4.5"/><path d="M29 58c0-6 4-9 9-9s9 3 9 9"/>
      <circle cx="60" cy="45" r="4.5"/><path d="M51 58c0-6 4-9 9-9s9 3 9 9"/>
      <path d="M38 36c6-6 16-6 22 0"/><path d="M57 33l3 3-4 1"/>
      <path d="M60 64c-6 6-16 6-22 0"/><path d="M41 67l-3-3 4-1"/>
    </svg>
    <h2 class="feature-title">LINKS &amp; RESOURCES</h2>
    <p class="feature-text">View recommended websites and other valuable resources.</p>
    <a class="feature-btn" href="#">Click Here</a>
  </section>

  <section class="feature" style="left:596px">
    <svg class="feature-icon" width="98" height="98" viewBox="0 0 98 98" fill="none" stroke="var(--leaf)" stroke-width="1.6">
      <circle cx="49" cy="49" r="47.5"/>
      <path d="M34 52l14-12 12 14-14 12z"/>
      <path d="M40 44l16-8 8 16-16 8"/>
      <path d="M46 38l18-4 4 18"/>
      <line x1="52" y1="41" x2="62" y2="39"/><line x1="53" y1="45" x2="63" y2="43"/><line x1="54" y1="49" x2="64" y2="47"/>
    </svg>
    <h2 class="feature-title">HELPFUL FORMS</h2>
    <p class="feature-text">Click here to view and print forms for your appointment.</p>
    <a class="feature-btn" href="#">Click Here</a>
  </section>

  <svg class="footer-wave" width="895" height="210" viewBox="0 0 895 210">
    <path fill="var(--leaf)" d="M0 70 C150 5 400 -5 620 60 C760 98 840 60 895 8 V210 H0 Z"/>
    <path fill="var(--sky)" d="M0 88 C200 30 420 22 620 80 C760 112 850 72 895 14 V210 H0 Z"/>
  </svg>

  <footer class="footer">
    <div class="social" aria-label="Social links"><span></span><span></span><span></span></div>
    <p class="footer-links">FAQ<span>/</span>Disclaimer<span>/</span>Terms<span>/</span>Privacy</p>
    <p class="copyright">© 2016 All Rights Reserved.</p>
  </footer>
</body>
</html>
```